Plakat-Design für Herbstausstellung
Zielgruppe
Wir sind im Motorradhandel, inkl. Motorrad Bekleidung/Zubehör, tätig. Für unsere Herbstausstellung brauchen wir ein neues Plakat-Design. Unsere Zielgruppe sind im allgemeinen Männer und Frauen im Alter von 18-65 Jahre.
Aufgabenstellung
Das Plakat sollte Hochformat sein.
Angaben welche ersichtlich sein sollten: Unser Logo (Velo Kranz);Herbst-Ausstellung; Datum der Herbstausstellung (20.-22.10.17); Öffnungszeiten (Fr. 14-19h/Sa. 8-19h/So. 9-16h); Saisonausverkauf mit -20% auf Motorradbekleidung und Zubehör (nur auf nicht reduzierte Lagerware); Unsere Livemusik im Festzelt ( Freitag ab 20.00 Uhr Vinyl Abend mit Dustrider, Samstag ab 20.00 Uhr Festmusik mit Bergklang-Ost, Sonntag Matinée 09.00-16.00 Uhr), www.velo-kranz.ch)<- kann klein dargestellt werden; Unsere Markenvertretungen (QRZ, FVL, Harimo)
Vom Design her ist der Kreativität keine Grenze gesetzt (In den Dateianhängen ist unser altes Plakat-Design beigefügt, als Anhaltspunkt für den Inhalt). Es sollte modern und einladend wirken. Wir verwenden im Normalfall den Font "Impact", dies stellt aber kein Killerkriterium dar.

```html
<!DOCTYPE html>
<html lang="de">
<head>
<meta charset="utf-8">
<title>Herbst Ausstellung – Velo Kranz</title>
<link href="https://fonts.googleapis.com/css2?family=Anton&family=Oswald:wght@400;600;700&family=Great+Vibes&display=swap" rel="stylesheet">
<style>
  :root{
    --stage:#c9d5db;
    --paper-top:#f3ddc8;
    --paper-bottom:#efd3bd;
    --red:#e0262b;
    --brown:#8a4a2a;
    --ribbon:#9b4b26;
    --ribbon-dark:#6e3219;
    --band:#f7f7f7;
    --leaf-orange:#e0782a;
    --leaf-red:#b93a1c;
    --soft:#e7a8a0;
    --ink:#5a3a2a;
    --partner:#2f4a5e;
  }
  *{margin:0;padding:0;box-sizing:border-box}
  html,body{width:1200px;height:900px;overflow:hidden;background:var(--stage)}
  .poster{
    position:absolute;left:310px;top:40px;width:580px;height:820px;
    background:linear-gradient(180deg,var(--paper-top),var(--paper-bottom));
    overflow:hidden;font-family:"Oswald",sans-serif;color:var(--red);
    box-shadow:0 10px 30px rgba(0,0,0,.15);
  }
  .leaves-top{position:absolute;left:0;top:0;width:380px;height:150px;
    background:radial-gradient(ellipse at 30% 0%,var(--leaf-red),var(--leaf-orange) 45%,rgba(240,170,80,.4) 70%,transparent 80%)}
  .leaves-bottom{position:absolute;right:0;bottom:0;width:300px;height:120px;
    background:radial-gradient(ellipse at 70% 100%,var(--leaf-orange),rgba(230,150,90,.5) 50%,transparent 75%)}
  .brand{position:absolute;right:28px;top:36px;display:flex;align-items:center;gap:8px;
    background:#fff;padding:8px 12px;font-family:"Anton",sans-serif;font-size:22px;color:var(--red);letter-spacing:.5px}
  .brand-mark{width:16px;height:16px;background:var(--red)}
  .title-script{position:absolute;left:0;right:0;top:110px;text-align:center;
    font-family:"Great Vibes",cursive;font-size:74px;color:var(--brown);transform:translateX(40px) rotate(-8deg)}
  .title-main{position:absolute;left:0;right:0;top:150px;text-align:center;
    font-family:"Anton",sans-serif;font-size:80px;letter-spacing:3px;color:var(--red);transform:rotate(8deg)}
  .deco-lines{position:absolute;left:0;top:200px;width:580px;height:120px}
  .ribbon{position:absolute;left:90px;top:248px;width:400px;height:60px;transform:rotate(8deg)}
  .hours{position:absolute;left:0;right:0;top:318px;text-align:center;font-weight:700;font-size:20px;transform:rotate(8deg)}
  .sale{position:absolute;left:0;right:0;top:365px;text-align:center;transform:rotate(8deg)}
  .sale-title{font-family:"Anton",sans-serif;font-size:34px;letter-spacing:1px;display:block}
  .sale-text{font-weight:600;font-size:19px;color:var(--red);display:block;line-height:1.1}
  .sale-note{font-size:10px;color:var(--brown);display:block}
  .band{position:absolute;left:-20px;top:470px;width:620px;height:90px;background:var(--band);
    transform:rotate(8deg);display:flex;align-items:center;justify-content:space-around;padding:0 60px;
    box-shadow:0 3px 8px rgba(0,0,0,.1)}
  .band-label{font-weight:700;font-size:12px;color:var(--red);line-height:1.1;text-align:center}
  .partner{display:flex;align-items:center;gap:6px;font-family:"Oswald",sans-serif;font-weight:700;font-size:16px;color:var(--ink)}
  .partner-dot{width:16px;height:16px;border-radius:50%;background:var(--ink)}
  .partner-badge{width:34px;height:34px;background:var(--partner)}
  .music{position:absolute;left:0;right:0;top:570px;text-align:center;transform:rotate(8deg)}
  .music-title{font-family:"Anton",sans-serif;font-size:34px;letter-spacing:1px;display:block}
  .music-sub{font-family:"Great Vibes",cursive;font-size:30px;color:var(--brown);display:block;margin-top:-12px}
  .days{position:absolute;left:20px;top:640px;width:560px;display:flex;transform:rotate(8deg)}
  .day{flex:1;text-align:center;border-left:1px solid rgba(138,74,42,.3);padding-top:8px}
  .day:first-child{border-left:none}
  .day-name{font-family:"Anton",sans-serif;font-size:40px;line-height:1}
  .day-time{font-size:12px;font-weight:700;vertical-align:top;display:inline-block;line-height:1.1;margin-left:4px}
  .day-time sup{font-size:8px}
  .day-act{font-size:13px;color:var(--brown);line-height:1.2;margin-top:4px}
  .day.faint{color:var(--soft)}
  .day.faint .day-act{color:var(--soft)}
  .contact{position:absolute;left:24px;bottom:28px;font-size:9px;color:var(--brown);line-height:1.3;transform:rotate(8deg);transform-origin:left bottom}
</style>
</head>
<body>
<main class="poster">
  <div class="leaves-top" role="img" aria-label="Herbstlaub in Rot und Orange"></div>
  <div class="leaves-bottom" role="img" aria-label="Herbstlaub am unteren Rand"></div>

  <div class="brand"><span class="brand-mark"></span>Velo Kranz</div>

  <div class="title-script">Herbst</div>
  <h1 class="title-main">AUSSTELLUNG</h1>

  <svg class="deco-lines" viewBox="0 0 580 120" aria-hidden="true">
    <path d="M40 60 Q120 90 210 110" stroke="#8a4a2a" stroke-width="1.5" fill="none"/>
    <path d="M360 150 Q450 150 540 170" stroke="#8a4a2a" stroke-width="1.5" fill="none"/>
  </svg>

  <svg class="ribbon" viewBox="0 0 400 60" aria-label="20. – 22. Oktober 2017">
    <polygon points="0,14 40,14 40,54 0,54 14,34" fill="var(--ribbon-dark)"/>
    <polygon points="400,14 360,14 360,54 400,54 386,34" fill="var(--ribbon-dark)"/>
    <rect x="30" y="4" width="340" height="44" fill="var(--ribbon)"/>
    <text x="200" y="35" text-anchor="middle" font-family="Oswald, sans-serif" font-weight="700" font-size="22" fill="#fff">20. – 22. OKTOBER 2017</text>
  </svg>

  <p class="hours">FR. 14-19 Uhr | SA. 8-19 Uhr | SO. 9-16 Uhr</p>

  <div class="sale">
    <span class="sale-title">SAISONABVERKAUF</span>
    <span class="sale-text">-20% auf Motorradbekleidung und Zubehör</span>
    <span class="sale-note">Nur auf nicht reduzierte Lagerware</span>
  </div>

  <div class="band">
    <span class="band-label">Unsere<br>Marken-<br>vertretung</span>
    <span class="partner"><span class="partner-dot"></span>QRZ</span>
    <span class="partner"><span class="partner-dot"></span>FVL</span>
    <span class="partner"><span class="partner-dot"></span>Harimo</span>
    <span class="partner-badge" role="img" aria-label="Partnerzeichen"></span>
  </div>

  <div class="music">
    <span class="music-title">LIVE-MUSIK</span>
    <span class="music-sub">im grossen Festzelt</span>
  </div>

  <div class="days">
    <div class="day">
      <span class="day-name">FR</span><span class="day-time">AB<br>20<sup>00</sup></span>
      <p class="day-act">Vinyl Abend<br>mit Dustrider</p>
    </div>
    <div class="day">
      <span class="day-name">SA</span><span class="day-time">AB<br>20<sup>00</sup></span>
      <p class="day-act">Festmusik mit<br>Bergklang-Ost</p>
    </div>
    <div class="day faint">
      <span class="day-name">SO</span><span class="day-time">AB<br>9<sup>00</sup>-16<sup>00</sup></span>
      <p class="day-act">Matinée</p>
    </div>
  </div>

  <p class="contact">Laubweg 12, 6300 Kranzingen<br>Tel. 041 555 12 34 · www.velo-kranz.ch</p>
</main>
</body>
</html>
```